Race car follow-up website needs web design

We are currently finalising a website which allows amateur and professional owners of race cars to track the running time of the car and all installed parts (drive shafts, gearbox etc.). The site is working for a technical point of view, but needs a nice design applied to it.

The website is made with Bootstrap 3.x and does not need a mobile skin. We target desktop and tablet users. This means that the delivered work should be easy to incorporate in the Bootstrap site that currently exists, from a technical point of view.

In attachment you can find all the screens that need skinning. If you think some stuff can be done better from a usability or design point of view (size of tables, placement of buttons etc.), do not hesitate to make a suggestion. We are open to positive criticism, and the current "base" design is not carved in stone. The colors currently used are basic Bootstrap so that can change too. There are no limits whatsoever, as long as the result looks good.

We have a big amount of racing/racecar/mechanic/pitbox related photo material that can be used, so do not hesitate to ask for material if needed.

The start page should be something along the lines of these sites:

https://plumvex.me/
http://quorvane.io/
https://teldrova.com/
http://www.mivostrel.com/

Or in words: a top navigation bar (as seen in the screenshots). A full-width image relevant to the content (racing related) with some text in overlay (A sort of slogan along the lines of "Let us track your parts" or "Parts tracking for you race or trackday car" ). Under that image there should then be a very high-level overview of what the website can be used for (In a few steps, with graphics/photos, schematics, showing driving the car, data transfer, management in the site.). This so the potential user can quickly see if it is of any interest to him/her.

Basically:

Drive --- Download data -- Get Alerted

each step should contain an "icon" representing what it is about, and a few lines of text explaining what is meant.

On that page (in the image part, or below the explanation) there should be 2 links (buttons). One leads to the pricing page, one to the registration page.

Of course this first page cannot be finalised until we give the complete details of the content, so please provide a high-level design and the person I work with will receive the detailed specs (the text for the different steps etc).

The other screens are (we think) self-explanatory. Please look at them in chronological order (they are prefixed 00 to 19)

There are screenshots of the manual. This page will also need to be styled (to match the rest of the site and to make the layout a bit more sexy). We will of course provide the original html file to this once the content needs to be finalised.

Besides the website, a mail template is required too. The site sends mails for:
- registration confirmation
- lost password
- alerts related to the car parts or the data files.

These mails should also have a professional looking skin (right now they are plain text)

Just to make things clear, if you think the base design we made is "crap", please suggest improvements (for instance, menu placement in the bottom, positioning of certain elements, tables that might be better off somewhere else, the car details on top that take too much screen real-estate etc. etc.). This site has been built by developers, not by designers. The only condition is that it should be technically possible in a reasonable amount of time using Bootstrap 3.x

Please provide the resources in such a way that a developer with web skills can directly implement them. So any slicing of graphics should be done by the designer. If you only provide us a good looking psd file we won't be able to do anything with that, unfortunately.

If you, as a designer, have a passion for sports cars, race cars, trackdays and/or GT car racing, this is of course a plus. The collaboration will be a lot easier if we speak the same "language".

Please provide at least a design of
- the start page
- the "car details" page
- one of the list modals
- one of the form modals

so we can at least know how the rest of the pages will look

The name is Pitlane Ledger.

Some pictures that can be used:

https://www.snapvelo.com/photos/58310472@K04/20581937466/
https://www.snapvelo.com/photos/58310472@K04/4815209367/
https://www.snapvelo.com/photos/58310472@K04/4812766058/
https://www.snapvelo.com/photos/58310472@K04/4801533729/
https://www.snapvelo.com/photos/58310472@K04/4763921850/
https://www.snapvelo.com/photos/58310472@K04/4706418592/
https://www.snapvelo.com/photos/58310472@K04/4594071683/
https://www.snapvelo.com/photos/58310472@K04/4361829074/
https://www.snapvelo.com/photos/58310472@K04/3958316247/
https://www.snapvelo.com/photos/58310472@K04/3927140568/
https://www.snapvelo.com/photos/58310472@K04/3915762839/
https://www.snapvelo.com/photos/58310472@K04/3915764901/
https://www.snapvelo.com/photos/58310472@K04/3890417352/
https://www.snapvelo.com/photos/58310472@K04/3885093716/
https://www.snapvelo.com/photos/58310472@K04/3885097284/
https://www.snapvelo.com/photos/58310472@K04/2081359647/
https://www.snapvelo.com/photos/58310472@K04/2398640513/
https://www.snapvelo.com/photos/58310472@K04/2486075129/
https://www.snapvelo.com/photos/58310472@K04/2323149876/
https://www.snapvelo.com/photos/58310472@K04/2323154902/

Basically you take whatever you want from this guy’s photo stream:
https://www.snapvelo.com/photos/58310472@K04/

I know him personally so there should be no copyright issues.

Most users of the site will run so called "GT" cars (Valdorni, Castruzzo etc.), so please refrain from using (or referencing) open wheelers, F1, LMP etc.

There is a logo contest too: http://gigs.pixelbazaar.com/gig.aspx?id=837461

I just updated the brief with some more info and images you can use.

I have updated the brief. This is added: for the first screen, the schematics are explained in a bit more detail: Basically: Drive ---> Download data --> Get Alerted each step should contain an "icon" representing what it is about, and a few lines of text explaining what is meant.

Dear designers, As we have received numerous remarks about our contest from you and your colleagues we have contacted PixelBazaar to solve the situation. This contest will be split into two different contests. One logo design contest for $400 and one website design contest for the $1480. Everyone who has submitted logos can of course participate with those logos in the logo design contest (there are a few that we like, which have been submitted). We are very sorry for the inconvenience we might have caused, and if you want to redraw your designs already submitted because of this we will fully understand this, but we hope this decision will make things clearer for everyone participating. As soon as matters are changed we will send you all a new message with the updated information. Thanks for your understanding. Morlek BVBA

The logo contest has been created: http://gigs.pixelbazaar.com/gig.aspx?id=837461

Reason: Because of the split in webdesign / logo the deadline has been extended so non-logo webdesigners can participate too. Logo project: http://gigs.pixelbazaar.com/gig.aspx?id=837461

The pricing page has been added in the screenshots section

Trackday enthousiasts, race car owners, race teams.

• No video
No huge "footer" with a lot of links to navigate the site, since there will be very litte content.
No references to non-GT type cars (so no F1, no Series Quelmont, no LMP1/LMP2) or street cars.

```html
<!DOCTYPE html>
<html lang="en">
<head>
<meta charset="utf-8">
<title>Pitlane Ledger</title>
<link href="https://fonts.googleapis.com/css2?family=Carlito:wght@400;700&display=swap" rel="stylesheet">
<style>
  :root {
    --black: #050505;
    --ink: #111111;
    --lime: #a4bf3c;
    --lime-dark: #7f9530;
    --trace: #66752a;
    --white: #ffffff;
    --grey-mid: #555555;
    --footer-ink: #111111;
  }
  * { margin: 0; padding: 0; box-sizing: border-box; }
  html, body { width: 1200px; height: 971px; overflow: hidden; background: var(--white); }
  body { font-family: "Carlito", "Calibri", sans-serif; position: relative; }

  .site-header {
    position: absolute; left: 0; top: 0; width: 1200px; height: 88px;
    background: var(--black); overflow: hidden;
  }
  .header-watermark {
    position: absolute; left: 345px; top: -6px;
    font-size: 96px; font-weight: 700; letter-spacing: 4px;
    color: #222222; white-space: nowrap; text-transform: uppercase;
  }
  .brand {
    position: absolute; left: 120px; top: 28px;
    display: flex; align-items: center; gap: 10px;
    font-size: 24px; font-weight: 700; color: var(--white); white-space: nowrap;
  }
  .brand-dot { width: 10px; height: 10px; border-radius: 50%; background: var(--lime); }
  .main-nav { position: absolute; right: 128px; top: 58px; display: flex; gap: 15px; }
  .main-nav a { color: var(--white); text-decoration: none; font-size: 21px; }
  .main-nav a.is-active { color: var(--lime); }
  .header-rule {
    position: absolute; left: 0; top: 88px; width: 1200px; height: 8px;
    background: linear-gradient(to right, #6c6c6c, #d0d0d0 60%, #f2f2f2);
  }

  .hero { position: absolute; left: 0; top: 96px; width: 1200px; height: 456px; }
  .hero-photo {
    position: absolute; inset: 0;
    background:
      radial-gradient(ellipse 320px 200px at 900px 320px, #b3c24a 0%, rgba(150,170,60,0.6) 45%, rgba(0,0,0,0) 100%),
      linear-gradient(to bottom, #3e3e3e 0%, #7a7a78 25%, #55554f 45%, #8a8d7c 70%, #9a9a98 88%, #d8d8d8 100%);
  }
  .hero-band {
    position: absolute; left: 0; top: 195px; width: 660px; height: 50px;
    background: linear-gradient(to right, #7f9133, #8ea03a 70%, rgba(142,160,58,0));
  }
  .hero-slogan {
    position: absolute; left: 86px; top: 198px;
    font-size: 37px; color: var(--white);
  }
  .hero-lead {
    position: absolute; left: 86px; top: 265px;
    font-size: 26px; line-height: 29.5px; color: var(--lime);
  }

  .steps {
    position: absolute; left: 0; top: 552px; width: 1200px; height: 348px;
    background: linear-gradient(to bottom, #1a1a1a 0%, #262626 30%, #3c3c3c 70%, #6a6a6a 100%);
    overflow: hidden;
  }
  .steps-traces { position: absolute; left: 0; top: 0; }
  .steps-brand {
    position: absolute; left: 0; width: 1200px; top: 6px; text-align: center;
    font-size: 50px; font-weight: 700; color: var(--white);
  }
  .step-title {
    position: absolute; top: 92px; width: 400px; margin-left: -200px; text-align: center;
    font-size: 21px; color: var(--white);
  }
  .step-title span { color: var(--lime); }
  .step-card {
    position: absolute; top: 133px; height: 151px;
    background: linear-gradient(to bottom, #121212 0%, #0b0b0b 88%, #2a2a2a 89%, #2a2a2a 100%);
    border-radius: 10px 10px 8px 8px;
    box-shadow: 0 2px 3px rgba(0,0,0,0.6);
    display: flex; align-items: center; justify-content: center;
  }
  .step-card svg { margin-top: -12px; }
  .cta {
    position: absolute; top: 294px; height: 36px;
    background: linear-gradient(to bottom, #b9d254 0%, #a4bf3c 40%, #8ea535 100%);
    box-shadow: 2px 3px 3px rgba(0,0,0,0.45);
    color: var(--white); font-size: 28px; text-decoration: none;
    display: flex; align-items: center; justify-content: center;
  }

  .site-footer {
    position: absolute; left: 0; top: 900px; width: 1200px; height: 71px;
    background: linear-gradient(to bottom, #e4e4e4 0%, #ffffff 20%);
  }
  .site-footer p {
    text-align: center; margin-top: 30px; font-size: 17px; color: var(--footer-ink);
  }
</style>
</head>
<body>
  <header class="site-header">
    <div class="header-watermark">Pitlane Ledger</div>
    <div class="brand"><span class="brand-dot"></span>Pitlane Ledger</div>
    <nav class="main-nav">
      <a href="#" class="is-active">Home</a>
      <a href="#">Register</a>
      <a href="#">My cars</a>
      <a href="#">Contct us</a>
    </nav>
  </header>
  <div class="header-rule"></div>

  <section class="hero">
    <div class="hero-photo" role="img" aria-label="Lime and white GT race car cornering at speed on a track with motion-blurred background"></div>
    <div class="hero-band"></div>
    <h1 class="hero-slogan">Parts tracking for you race</h1>
    <p class="hero-lead">Lorem ipsum dolor sit amet,<br>consectetur adipisicing elit,<br>sed do eiusmod tempor.</p>
  </section>

  <section class="steps">
    <svg class="steps-traces" width="1200" height="348" viewBox="0 0 1200 348" aria-hidden="true">
      <g stroke="var(--trace)" stroke-width="6" fill="none">
        <line x1="0" y1="161" x2="1200" y2="161"/>
        <line x1="0" y1="189" x2="1200" y2="189"/>
        <line x1="0" y1="220" x2="1200" y2="220"/>
        <line x1="0" y1="248" x2="1200" y2="248"/>
        <line x1="240" y1="303" x2="960" y2="303"/>
      </g>
    </svg>

    <div class="steps-brand">Pitlane Ledger</div>

    <h2 class="step-title" style="left:190px">1| <span>Do your magic!</span></h2>
    <h2 class="step-title" style="left:610px">2| <span>Transfer data</span></h2>
    <h2 class="step-title" style="left:1036px">3| <span>Analize status</span></h2>

    <div class="step-card" style="left:25px; width:308px">
      <svg width="110" height="92" viewBox="0 0 110 92" aria-label="Chequered flag">
        <g transform="rotate(18 55 46)" fill="var(--white)">
          <rect x="10" y="10" width="14" height="10"/><rect x="38" y="10" width="14" height="10"/><rect x="66" y="10" width="14" height="10"/>
          <rect x="24" y="20" width="14" height="10"/><rect x="52" y="20" width="14" height="10"/><rect x="80" y="20" width="10" height="10"/>
          <rect x="10" y="30" width="14" height="10"/><rect x="38" y="30" width="14" height="10"/><rect x="66" y="30" width="14" height="10"/>
          <rect x="84" y="36" width="10" height="50" rx="3"/>
        </g>
      </svg>
    </div>
    <div class="step-card" style="left:455px; width:307px">
      <svg width="110" height="92" viewBox="0 0 110 92" aria-label="Laptop">
        <g fill="none" stroke="var(--white)" stroke-width="9" stroke-linejoin="round">
          <path d="M20 52 L48 6 L102 36 L74 82 Z"/>
        </g>
        <path d="M6 54 L58 54 L74 86 L22 86 Z" fill="var(--white)"/>
      </svg>
    </div>
    <div class="step-card" style="left:869px; width:306px">
      <svg width="90" height="80" viewBox="0 0 90 80" aria-label="Line chart">
        <path d="M12 6 V70 H82" fill="none" stroke="var(--white)" stroke-width="10" stroke-linecap="round"/>
        <path d="M22 30 L42 58 L64 24 L80 8" fill="none" stroke="var(--white)" stroke-width="9" stroke-linejoin="round" stroke-linecap="round"/>
      </svg>
    </div>

    <a href="#" class="cta" style="left:20px; width:197px">Pricing</a>
    <a href="#" class="cta" style="left:980px; width:196px">Registration</a>
  </section>

  <footer class="site-footer">
    <p>Copyright 2014 Pitlane Ledger | All rights reserved.</p>
  </footer>
</body>
</html>
```